Simple one page Wordpress website

We need a quick turnaround single page wordpress website.
The design needs to be very simple and clean.
We already have some design assets (logos and colours etc) and some draft copy for the page.

We need all the files for us to be able to create a wordpress site. We can do this ourselves and we will host it.

```html
<!DOCTYPE html>
<html lang="en">
<head>
<meta charset="utf-8">
<title>Halcyra – Working with Veterinarians</title>
<link href="https://fonts.googleapis.com/css2?family=Poppins:ital,wght@0,300;0,400;0,500;0,600;0,700;1,400&display=swap" rel="stylesheet">
<style>
:root{
  --blue:#2f7fc0;
  --blue-deep:#1f6aa8;
  --blue-light:#5fa3d8;
  --green:#8aab12;
  --green-text:#86a911;
  --steel:#5289bd;
  --grey:#e6e6e6;
  --form:#dde7f0;
  --ink:#333;
  --footer:#3a5244;
  --white:#fff;
}
*{box-sizing:border-box;margin:0;padding:0}
html,body{width:1200px;height:4738px;overflow:hidden}
body{position:relative;font-family:'Poppins',sans-serif;color:var(--ink);background:var(--white)}
.abs{position:absolute}
section,header,footer{position:absolute;left:0;width:1200px}

/* hero */
.hero{top:0;height:575px;background:linear-gradient(180deg,var(--blue-deep) 0%,var(--blue) 55%,var(--blue-light) 100%);overflow:hidden}
.hero-curve{position:absolute;left:-120px;top:460px;width:1440px;height:500px;border-radius:50%;background:var(--white)}
.brand{font-weight:600;font-size:30px;letter-spacing:0;color:var(--white);line-height:1}
.nav{position:absolute;top:44px;font-size:13px;color:var(--white)}
.nav a{position:absolute;white-space:nowrap;color:inherit;text-decoration:none}
.nav a.active{color:#9fd31a}
.hero-title{left:171px;top:245px;font-size:36px;font-weight:700;line-height:42px;color:var(--white)}
.hero-photo{left:470px;top:129px;width:202px;height:313px;border-radius:90px 90px 40px 40px;background:linear-gradient(180deg,#c9a98c 0%,#e7b23a 55%,#b78f6c 100%)}
.hero-copy{left:771px;top:221px;width:258px;font-size:15px;line-height:20.5px;color:var(--white);text-align:justify;font-weight:300}

/* about */
.about-photo{left:171px;top:567px;width:422px;height:304px;border-radius:28px;background:linear-gradient(135deg,#f1f2f3 0%,#dfe3e6 45%,#4a3a33 70%,#e8ebed 100%)}
.about-title{left:631px;top:582px;font-size:34px;font-weight:700;color:var(--green-text)}
.about-copy{left:631px;top:638px;width:398px;font-size:12.5px;line-height:16.5px}
.about-copy p+p{margin-top:16px}
.read-more{left:631px;top:850px;font-size:15px;font-style:italic}

/* why */
.why{top:972px;height:624px;background:var(--green);color:var(--white)}
.eyebrow{font-size:15px;font-style:italic}
.why .eyebrow{position:absolute;left:171px;top:190px}
.why-title{left:171px;top:212px;font-size:36px;font-weight:700;line-height:43px}
.why-copy{left:171px;top:362px;width:390px;font-size:12.5px;line-height:16.5px}
.why-photo{left:606px;top:141px;width:423px;height:350px;background:linear-gradient(160deg,#eef1f3 0%,#cfd8de 40%,#f3ece4 70%,#7a8a96 100%)}

/* services */
.services{top:1596px;height:764px;background:var(--grey)}
.services .eyebrow{position:absolute;left:171px;top:102px}
.section-title{font-size:36px;font-weight:700;color:var(--green-text)}
.services .section-title{position:absolute;left:171px;top:122px}
.services-copy{left:171px;top:180px;width:858px;font-size:12.5px;line-height:16.5px}
.card{top:274px;width:396px;height:377px;color:var(--white);overflow:hidden}
.card-collection{left:171px;background:linear-gradient(180deg,#8dd9b8 0%,#2f8a4f 45%,#0f4a24 100%)}
.card-data{left:633px;background:linear-gradient(180deg,#4d4a46 0%,#6d7f97 40%,#1c2430 100%)}
.card-title{position:absolute;left:12px;font-size:35px;font-weight:700}
.card-list{position:absolute;left:15px;right:15px;font-size:13px;line-height:16.5px;list-style:none}
.card-arrow{position:absolute;top:108px;width:48px;height:48px;border-radius:50%;background:rgba(255,255,255,.35)}
.card-arrow svg{position:absolute;left:14px;top:14px}

/* testimonials */
.testimonials{top:2360px;height:329px;text-align:center}
.testimonials .eyebrow{position:absolute;left:0;width:1200px;top:70px}
.testimonials .section-title{position:absolute;left:0;width:1200px;top:95px}
.quote{left:300px;top:160px;width:600px;font-size:13px;line-height:16.5px}
.quote-by{left:0;width:1200px;top:196px;font-size:16px;font-style:italic;color:var(--green-text)}
.dots{left:556px;top:250px;display:flex;gap:9px}
.dots span{width:15px;height:15px;border-radius:50%;background:var(--steel)}
.dots span.on{background:var(--green)}

/* partners */
.partners{top:2689px;height:942px;background:var(--steel);color:var(--white)}
.partners .eyebrow{position:absolute;left:171px;top:100px}
.partners-title{left:171px;top:120px;font-size:36px;font-weight:700}
.partner-name{top:222px;font-size:36px;font-weight:700;left:12px}
.partner{position:absolute;top:0;width:396px}
.partner-photo{position:absolute;top:269px;left:0;width:396px;height:383px;background:linear-gradient(180deg,#4f86bb 0%,#3e6f9e 35%,#2a3a4d 100%)}
.partner-bio{position:absolute;top:672px;left:0;width:362px;font-size:12.5px;line-height:16.5px;text-align:justify}
.partner-bio p+p{margin-top:16px}

/* contact */
.contact{top:3631px;height:700px}
.contact .eyebrow{position:absolute;left:171px;top:226px;font-size:14px}
.contact-title{left:171px;top:244px;font-size:36px;font-weight:700;color:var(--steel)}
.contact-copy{left:171px;top:303px;width:365px;font-size:12.5px;line-height:16.5px}
.write-label{left:171px;top:457px;font-size:12px}
.write-email{left:171px;top:474px;font-size:36px;font-weight:700;color:var(--steel)}
.form{left:576px;top:181px;width:453px;height:418px;background:var(--form)}
.form-title{position:absolute;left:24px;top:16px;font-size:34px;font-weight:700;color:var(--steel)}
.field{position:absolute;left:28px;width:336px;border:1.5px solid var(--steel);background:var(--form);font-size:13px;padding:9px 20px;color:#444}
.send{position:absolute;left:239px;top:359px;width:125px;height:31px;background:var(--steel);color:var(--white);font-size:13px;text-align:center;line-height:31px}

/* social + footer */
.social{left:171px;top:4331px;width:317px;height:49px;background:var(--green);display:flex;align-items:center;justify-content:space-around;padding:0 22px}
.social span{width:13px;height:13px;border-radius:50%;background:var(--white)}
.footer{top:4380px;height:308px;background:var(--footer);color:var(--white)}
.footer .brand{position:absolute;left:171px;top:62px}
.footer-col{position:absolute;top:48px}
.footer-col h3{font-size:26px;font-weight:600;margin-bottom:6px}
.footer-col ul{list-style:none;font-size:13px}
.footer-col li{height:35px;line-height:35px}
.copyright{left:0;width:1200px;top:4710px;text-align:center;font-size:12px;font-weight:500}
</style>
</head>
<body>

<header class="hero">
  <div class="hero-curve"></div>
  <div class="abs brand" style="left:171px;top:38px">Halcyra</div>
  <nav class="nav">
    <a class="active" style="left:488px">Home</a>
    <a style="left:565px">About ORVEX</a>
    <a style="left:670px">Why ORVEX</a>
    <a style="left:764px">Our Team</a>
    <a style="left:865px">Sectors</a>
    <a style="left:953px">Contact Us</a>
  </nav>
  <h1 class="abs hero-title">Working with<br>Veterinarians</h1>
  <div class="abs hero-photo" role="img" aria-label="Small dog in a yellow jumper sitting and looking back over its shoulder"></div>
  <p class="abs hero-copy">Regardless of whether ORVEX is dealing with humans or animals, at its core the systems and processes remain the same. Efficient, secure data collection, analysis and date reporting are crucial in both fields.</p>
</header>

<section class="about-block" style="top:0;height:0">
  <div class="abs about-photo" role="img" aria-label="Doctor in a white coat with stethoscope holding a smartphone"></div>
  <h2 class="abs about-title">About ORVEX</h2>
  <div class="abs about-copy">
    <p>Although primarily developed for the testing and diagnosis of human conditions, ORVEX lends itself equally to the treatment of animals. There are several modules that are animal-specific, for both livestock veterinarians and those who treat domestic pets.</p>
    <p>The Agri-food and Equine care market is worth over £90Bn in the UK, yet tests are largely conducted and recorded by hand. ORVEX is particularly relevant when large numbers of tests need to be delivered and analysed quickly to manage herd welfare and avoid potential losses in profitability or the spread of damaging conditions.</p>
  </div>
  <a class="abs read-more">Read More&gt;&gt;</a>
</section>

<section class="why">
  <p class="eyebrow">Why ORVEX</p>
  <h2 class="abs why-title">Capitalising<br>on the latest<br>IT technologies</h2>
  <p class="abs why-copy">ORVEX has deployed a SaaS cloud based software platform utilising the latest agile development disciplines to maximise the efficient, timely and secure collection, distribution, analysis and reporting of clinical data.</p>
  <div class="abs why-photo" role="img" aria-label="Scientist in a laboratory looking into a microscope"></div>
</section>

<section class="services">
  <p class="eyebrow">Services</p>
  <h2 class="section-title">Our services include:</h2>
  <p class="abs services-copy">By partnering with experts at every part of the chain, we ensure that our processes continue to meet the exacting standards of the healthcare professionals and laboratories we work with across the world, as well as satisfying every legal requirement for the security and storage of patient data.</p>

  <div class="abs card card-collection" role="img" aria-label="Gloved hand placing a test tube into a green sample rack">
    <span class="card-arrow" style="left:16px"><svg width="20" height="20" viewBox="0 0 20 20"><path d="M14 3 5 10l9 7z" fill="#fff"/></svg></span>
    <h3 class="card-title" style="top:230px">Collection</h3>
    <ul class="card-list" style="top:288px">
      <li>-&nbsp; Personal Details</li>
      <li>-&nbsp; Creation of a unique 'marker' for every test Appropriate user/clinician instructions Concise, relevant testing only</li>
    </ul>
  </div>

  <div class="abs card card-data" role="img" aria-label="Hand holding a phone in front of a laptop showing data charts">
    <span class="card-arrow" style="right:16px"><svg width="20" height="20" viewBox="0 0 20 20"><path d="M6 3l9 7-9 7z" fill="#fff"/></svg></span>
    <h3 class="card-title" style="top:210px">Data Management</h3>
    <ul class="card-list" style="top:272px">
      <li>-&nbsp; Secure deployment of test materials and data</li>
      <li>-&nbsp; Highly encrypted data transfer</li>
      <li>-&nbsp; Rapid accessibility for clinicians</li>
      <li>-&nbsp; Archiving and secure storage for verification and referral</li>
    </ul>
  </div>
</section>

<section class="testimonials">
  <p class="eyebrow">Testimonials</p>
  <h2 class="section-title">What They Say</h2>
  <p class="abs quote">In our work we perform testing at corporate gatherings and the app makes the process run a lot more smoothly."</p>
  <p class="abs quote-by">Marcus Fenwick, Managing Director Alder Health.</p>
  <div class="abs dots"><span></span><span></span><span class="on"></span><span></span></div>
</section>

<section class="partners">
  <p class="eyebrow">Partners</p>
  <h2 class="abs partners-title">The company’s founding partners are:</h2>
  <div class="partner" style="left:171px">
    <h3 class="abs partner-name">Graham Ashby</h3>
    <div class="partner-photo" role="img" aria-label="Portrait of founding partner Graham Ashby"></div>
    <div class="partner-bio"><p>Over the last 30 years Graham worked with start-ups and small technology companies, both in the UK and USA, and been instrumental in 5 exits totalling around £200 million. He recently set up Veriscan, a software and testing solution for Covid in the occupational health and travel sectors. He has an MBA from Halden Business School, an MA from Kestrel University, and is a qualified accountant. He is the Treasurer of the Halden Business School Club of London, and a Mentor on the National Health Board Clinical Entrepreneurs Programme.</p></div>
  </div>
  <div class="partner" style="left:633px">
    <h3 class="abs partner-name">Peter Lindqvist</h3>
    <div class="partner-photo" role="img" aria-label="Portrait of founding partner Peter Lindqvist"></div>
    <div class="partner-bio"><p>Peter studied Zoology at the University of Northdale and has a Master’s Degree in Biology from Westbridge University. He went on to become Chief Technology Officer at Solent Health, IT Project Manager with Brightmark Limited and co-founded Three Owls, a company that helps to safeguard travellers against the hazards of diseases they would not normally encounter at home.</p><p>He is a Director and co-founder of Veriscan with Graham Ashby.</p></div>
  </div>
</section>

<section class="contact">
  <p class="eyebrow">GET IN TOUCH</p>
  <h2 class="abs contact-title">Contact us</h2>
  <p class="abs contact-copy">Please get in touch with us if you are: a pharmacist looking to extend and improve your customer services, a clinician who would like to speed up and streamline the time between testing and diagnosis and the quality of information, or a laboratory who would like to provide a better service to your customers.</p>
  <p class="abs write-label">Write Us At</p>
  <p class="abs write-email">info@orvexmail.com</p>
  <div class="abs form">
    <h3 class="form-title">Send A Message</h3>
    <div class="field" style="top:77px;height:38px">Type name here</div>
    <div class="field" style="top:145px;height:38px">your email address</div>
    <div class="field" style="top:213px;height:117px">Type message here</div>
    <div class="send">Send Message</div>
  </div>
</section>

<div class="abs social" aria-label="Social links"><span></span><span></span><span></span><span></span></div>

<footer class="footer">
  <div class="brand">Halcyra</div>
  <div class="footer-col" style="left:453px">
    <h3>Menu</h3>
    <ul><li>Home</li><li>About ORVEX</li><li>Why ORVEX</li><li>Our Team</li><li>Sectors</li><li>Contact Us</li></ul>
  </div>
  <div class="footer-col" style="left:692px">
    <h3>Sectors</h3>
    <ul><li>Clinical Trial Data Collection</li><li>Occupational Health</li><li>Pathology &amp; Laboratories</li><li>Supporting Genetic Medical Research</li><li>Veterinarians</li></ul>
  </div>
</footer>
<p class="abs copyright">All Rights Reserved 2022</p>

</body>
</html>
```